Book Cover Design - "Lanterns Seldom Wander"

Looking for an eye-catching but professional book cover.

This book is designed to help people figure out why they hate their job and what to do about it.

The audience for this book is 18-35 year olds who feel stuck in their current roles. The theory here is that people often wind up in a job they don't love, then settle because they don't realize they can make things better.

The writer's style is clever and balances humor with practical advice.

```html
<!DOCTYPE html>
<html lang="en">
<head>
<meta charset="utf-8">
<title>Lanterns Seldom Wander – Book Cover</title>
<link rel="stylesheet" href="https://fonts.googleapis.com/css2?family=Inter:wght@300&display=swap">
<style>
  :root {
    --page-bg: #ffffff;
    --cover-frame: #000000;
    --scene-deep: #020a03;
    --scene-dark: #17401d;
    --scene-mid: #1f5a28;
    --scene-glow: #2a8a3c;
    --title-ink: #ffffff;
  }
  html, body {
    margin: 0;
    padding: 0;
    width: 1200px;
    height: 1000px;
    overflow: hidden;
    background: var(--page-bg);
  }
  .canvas {
    position: relative;
    width: 1200px;
    height: 1000px;
  }
  .book-cover {
    position: absolute;
    left: 334px;
    top: 42px;
    width: 617px;
    height: 918px;
    background: var(--cover-frame);
    box-sizing: border-box;
    padding: 8px 10px 10px 12px;
  }
  .cover-art {
    position: relative;
    width: 100%;
    height: 100%;
    overflow: hidden;
    background:
      radial-gradient(ellipse 260px 200px at 75% 28%, var(--scene-glow) 0%, transparent 70%),
      radial-gradient(ellipse 200px 160px at 10% 52%, var(--scene-glow) 0%, transparent 70%),
      radial-gradient(ellipse 300px 220px at 85% 60%, var(--scene-mid) 0%, transparent 75%),
      linear-gradient(180deg, var(--scene-dark) 0%, var(--scene-mid) 45%, #163f1c 68%, #081a0a 85%, var(--scene-deep) 100%);
  }
  .book-title {
    position: absolute;
    left: 20px;
    top: 72px;
    margin: 0;
    font-family: "Inter", "Helvetica Neue", Arial, sans-serif;
    font-weight: 300;
    font-size: 98px;
    line-height: 108px;
    letter-spacing: -1px;
    color: var(--title-ink);
    text-transform: uppercase;
  }
  .book-title span { display: block; }
</style>
</head>
<body>
  <main class="canvas">
    <section class="book-cover">
      <div class="cover-art" role="img" aria-label="Misty green fog scene with shadowy figures walking through the haze">
        <h1 class="book-title">
          <span>Lanterns</span>
          <span>Seldom</span>
          <span>Wander</span>
        </h1>
      </div>
    </section>
  </main>
</body>
</html>
```